Restaurant needs a vertical banner for fried catfish

Our restaurant is looking for an eye-catching 78.75in. x 36in. vertical physical banner ad for our fried catfish. Photos for the fried catfish will be provided as a reference but we will also accept anything similar to the photo. We will be using the following as our receptacle: https://www.plorvista.com/banner-stand/retractable-banner-stands/
The design must incorporate the following flavor texts:
Fried Catfish
Always Fresh!
Made from Scratch
Hand-cut Fillets
The Best Catfish in Texas
Served with fries, hush puppies, and a 32oz fountain drink
Also available by the pound!
The final design should be creative, professional, and eye-catching for customers.
Updates
Need extra days to review
Colors
Designer to choose colors to be used in the design.
Requirements
Must have
- We are open to any and all design elements, albeit the 'flavor texts' should not overpower, but complement the fried catfish photo. 'Fried Catfish' can be used in lieu of a main title/logo.
Nice to have
- Transparent or textured backgrounds that can encompass any or all part of the banner such as a cutting board, shadows, abstract, etc to show depth are a plus.
- Use of vectors or objects such as ribbons or shapes to encapsulate the 'flavor texts' are also encouraged.

```html
<!DOCTYPE html>
<html lang="en">
<head>
<meta charset="utf-8">
<title>Fried Catfish – Vertical Banner</title>
<link rel="stylesheet" href="https://fonts.googleapis.com/css2?family=Yellowtail&family=Rubik:ital,wght@0,900;1,900&family=Signika:wght@600&family=Open+Sans:wght@400&display=block">
<style>
  :root {
    --red: #d10036;
    --brown: #683e08;
    --gold: #fdb92c;
    --teal: #5ac5cf;
    --navy: #0a0aa6;
    --white: #ffffff;
  }
  html, body {
    margin: 0;
    padding: 0;
    width: 1200px;
    height: 2625px;
    overflow: hidden;
    background: var(--white);
  }
  .banner { display: block; width: 1200px; height: 2625px; }
  .headline { font-family: "Rubik", "Arial Black", sans-serif; font-weight: 900; font-style: italic; }
  .headline-fried { fill: var(--red); }
  .headline-catfish { fill: var(--brown); }
  .headline-shadow { fill: var(--gold); }
  .tagline { fill: var(--teal); }
  .script-title { font-family: "Yellowtail", "Brush Script MT", cursive; fill: var(--brown); }
  .feature-list { font-family: "Open Sans", Arial, sans-serif; font-size: 44px; fill: var(--brown); }
  .serving-note { font-family: "Signika", Arial, sans-serif; font-weight: 600; font-size: 64px; fill: var(--brown); }
  .pound-note { font-family: "Rubik", "Arial Black", sans-serif; font-weight: 900; font-style: italic; font-size: 64px; fill: var(--red); }
  .band-gold { fill: var(--gold); }
  .band-brown { fill: var(--brown); }
  .band-red { fill: var(--red); }
  .flag-field { fill: var(--navy); }
  .flag-star { fill: var(--white); }
</style>
</head>
<body>
<svg class="banner" viewBox="0 0 1200 2625" xmlns="http://www.w3.org/2000/svg">
  <defs>
    <linearGradient id="platter-tones" x1="0" y1="0" x2="0.3" y2="1">
      <stop offset="0" stop-color="#e7c9a4"/>
      <stop offset="0.25" stop-color="#d98a3e"/>
      <stop offset="0.55" stop-color="#c9772e"/>
      <stop offset="0.8" stop-color="#e2a94e"/>
      <stop offset="1" stop-color="#d59b45"/>
    </linearGradient>
  </defs>

  <!-- Title block -->
  <g class="title-block">
    <g transform="translate(112 300) rotate(-8)">
      <text class="headline headline-shadow" x="8" y="8" font-size="230" textLength="555" lengthAdjust="spacingAndGlyphs">Fried</text>
      <text class="headline headline-fried" x="0" y="0" font-size="230" textLength="555" lengthAdjust="spacingAndGlyphs">Fried</text>
    </g>
    <g transform="translate(182 492) rotate(-8)">
      <text class="headline headline-shadow" x="10" y="10" font-size="265" textLength="880" lengthAdjust="spacingAndGlyphs">Catfish</text>
      <text class="headline headline-catfish" x="0" y="0" font-size="265" textLength="880" lengthAdjust="spacingAndGlyphs">Catfish</text>
    </g>
    <g transform="translate(340 628) rotate(-8)">
      <text class="headline tagline" x="0" y="0" font-size="140" textLength="800" lengthAdjust="spacingAndGlyphs">Always Fresh!</text>
    </g>
  </g>

  <!-- Photo zone with bands -->
  <polygon class="band-gold" points="0,764 1200,590 1200,635 0,805"/>
  <polygon points="0,805 1200,635 1200,1558 0,1743" fill="url(#platter-tones)" role="img" aria-label="Photo of golden fried catfish fillets piled on a plate of french fries"/>
  <polygon class="band-brown" points="0,1743 1200,1558 1200,1604 0,1789"/>
  <polygon class="band-gold" points="0,1789 1200,1604 1200,1645 0,1835"/>

  <!-- Script title -->
  <g transform="translate(210 1935) rotate(-8)">
    <text class="script-title" x="0" y="0" font-size="165" textLength="900" lengthAdjust="spacingAndGlyphs">The Best Catfish</text>
  </g>
  <g transform="translate(365 2040) rotate(-8)">
    <text class="script-title" x="0" y="0" font-size="185" textLength="460" lengthAdjust="spacingAndGlyphs">in Texas</text>
  </g>

  <!-- Texas flag stripe -->
  <polygon class="band-red" points="298,2158 1200,2004 1200,2055 298,2204"/>
  <polygon class="flag-field" points="230,2098 298,2086 298,2210 230,2222"/>
  <polygon class="flag-star" points="264,2132 270,2149 288,2149 274,2160 279,2177 264,2167 249,2177 254,2160 240,2149 258,2149"/>

  <!-- Features -->
  <text class="feature-list" text-anchor="end">
    <tspan x="1123" y="2150">Made</tspan>
    <tspan x="1123" y="2203">from Scratch</tspan>
    <tspan x="1123" y="2256">Hand-cut Fillets</tspan>
  </text>

  <!-- Serving info -->
  <text class="serving-note" text-anchor="middle">
    <tspan x="605" y="2370">Served with fries, hush puppies,</tspan>
    <tspan x="605" y="2440">and a 32oz fountain drink</tspan>
  </text>
  <text class="pound-note" x="603" y="2545" text-anchor="middle" textLength="1010" lengthAdjust="spacingAndGlyphs">Also available by the pound!</text>
</svg>
</body>
</html>
```